professional business card design for technology company

We are a small technology consulting firm, specialising in consulting based around Cloud and Managed services. Our colour scheme is yellow, blue and white, as you can see in the logos. Although we are based in melbourne australia, due to the nature of our work, our clients can be located anywhere. We are looking for a clean, professional, positive look - similar to our company logo

Target Market(s)

small business

Industry/Entity Type

Business

Contact Information for Business Card

eye catching, designed to incorporate some level of raised printing. Must contain website address, phone number, name and job title

Requirements
Must have
• Logo (attached) - use of the same colour scheme

```html
<!DOCTYPE html>
<html lang="en">
<head>
<meta charset="utf-8">
<title>Nubera Business Card</title>
<link rel="stylesheet" href="https://fonts.googleapis.com/css2?family=Montserrat:wght@500;700&family=Open+Sans:wght@400;600&display=swap">
<style>
  :root {
    --bg: #d9d6d2;
    --card: #f1f1f1;
    --ink: #555555;
    --ink-dark: #4a4a4a;
    --yellow: #f2cb05;
    --bar: #5a5a5a;
  }
  * { margin: 0; padding: 0; box-sizing: border-box; }
  html, body { width: 1200px; height: 960px; overflow: hidden; }
  body {
    background: var(--bg);
    display: flex;
    flex-direction: column;
    align-items: center;
    justify-content: center;
    gap: 30px;
    font-family: "Open Sans", sans-serif;
  }
  .card {
    position: relative;
    width: 760px;
    height: 434px;
    background: var(--card);
    box-shadow: 0 6px 18px rgba(0,0,0,0.18);
    overflow: hidden;
  }
  .brand {
    display: flex;
    align-items: center;
    gap: 18px;
  }
  .brand-dot {
    width: 30px; height: 30px;
    border-radius: 50%;
    background: var(--yellow);
  }
  .brand-name {
    font-family: "Montserrat", sans-serif;
    font-weight: 700;
    color: var(--ink);
    letter-spacing: -1px;
  }

  /* Front */
  .card-front .brand {
    position: absolute;
    left: 0; right: 0; top: 140px;
    justify-content: center;
  }
  .card-front .brand-name { font-size: 92px; }
  .card-front .brand-dot { width: 44px; height: 44px; }
  .front-url {
    position: absolute;
    left: 0; right: 0; bottom: 52px;
    text-align: center;
    font-size: 14px;
    letter-spacing: 7px;
    color: var(--ink);
  }

  /* Back */
  .card-back .brand {
    position: absolute;
    left: 60px; top: 150px;
  }
  .card-back .brand-name { font-size: 54px; }
  .divider-bar {
    position: absolute;
    left: 430px; top: 0;
    width: 26px; height: 100%;
    background: var(--bar);
  }
  .edge-tab {
    position: absolute;
    right: 0; top: 60px;
    width: 18px; height: 92px;
    background: var(--bar);
  }
  .contact-icon {
    position: absolute;
    left: 421px;
    width: 44px; height: 44px;
    background: var(--yellow);
    display: flex; align-items: center; justify-content: center;
  }
  .contact-icon svg { width: 20px; height: 20px; fill: var(--ink-dark); }
  .icon-phone { top: 168px; }
  .icon-mail { top: 232px; }
  .icon-web { top: 296px; }
  .person {
    position: absolute;
    left: 490px; top: 64px;
  }
  .person-name {
    font-family: "Montserrat", sans-serif;
    font-weight: 700;
    font-size: 21px;
    color: var(--ink-dark);
  }
  .person-name .surname { font-weight: 500; color: var(--yellow); }
  .person-title {
    font-size: 14px;
    color: var(--ink);
    letter-spacing: 0.5px;
  }
  .contact-line {
    position: absolute;
    left: 490px;
    font-size: 15px;
    font-weight: 600;
    color: var(--ink-dark);
    line-height: 44px;
  }
  .line-phone { top: 168px; }
  .line-mail { top: 232px; }
  .line-web { top: 296px; }
</style>
</head>
<body>

  <section class="card card-front">
    <div class="brand">
      <span class="brand-dot"></span>
      <span class="brand-name">Nubera</span>
    </div>
    <p class="front-url">www.nubera.com</p>
  </section>

  <section class="card card-back">
    <div class="brand">
      <span class="brand-dot"></span>
      <span class="brand-name">Nubera</span>
    </div>

    <div class="divider-bar"></div>
    <div class="edge-tab"></div>

    <div class="person">
      <p class="person-name">MARCO T. <span class="surname">REYES</span></p>
      <p class="person-title">PRINCIPAL</p>
    </div>

    <div class="contact-icon icon-phone">
      <svg viewBox="0 0 24 24" aria-hidden="true"><path d="M6.6 10.8c1.4 2.8 3.8 5.1 6.6 6.6l2.2-2.2c.3-.3.7-.4 1-.2 1.1.4 2.3.6 3.6.6.6 0 1 .4 1 1V20c0 .6-.4 1-1 1C10.6 21 3 13.4 3 4c0-.6.4-1 1-1h3.5c.6 0 1 .4 1 1 0 1.3.2 2.5.6 3.6.1.3 0 .7-.2 1z"/></svg>
    </div>
    <div class="contact-icon icon-mail">
      <svg viewBox="0 0 24 24" aria-hidden="true"><path d="M2 5h20v2l-10 6L2 7z"/><path d="M2 9l10 6 10-6v10H2z"/></svg>
    </div>
    <div class="contact-icon icon-web">
      <svg viewBox="0 0 24 24" aria-hidden="true"><circle cx="12" cy="12" r="10"/></svg>
    </div>

    <p class="contact-line line-phone">305-555-0142</p>
    <p class="contact-line line-mail">MarcoTReyes@nubera.com</p>
    <p class="contact-line line-web">www.nubera.com</p>
  </section>

</body>
</html>
```